Business Card Design Project - ol taviran group

dear Sirs

we need business card design for our group ( OL Taviran Group ) , i have got the Logo design of our group from pixel forum in previous , so all need details relating to our group i think available with you, as well as the the chosen logo design

we hope to provide us with business card logo that to be appropaite and satisfactory to us .

thanks

note : logo design of our group is attached .

Reason: please extend the deadline of my project for additional 15 days because i didn't received appropriate design for our gruop yet . kindly beaware that i have received 77 design till now , supossed to send me 200-250 design at least . thanks

contents

name : Selim OR Haddani

position : Operation Manager

• person name

group logo
• logo color matching with back background

```html
<!DOCTYPE html>
<html lang="en">
<head>
<meta charset="utf-8">
<title>OL Taviran Group – Business Card</title>
<link rel="stylesheet" href="https://fonts.googleapis.com/css2?family=Arimo:wght@400;700&family=Libre+Baskerville:wght@400;700&display=swap">
<style>
  :root {
    --brand-blue: #0f4c8d;
    --brand-gold: #ead08f;
    --paper: #ffffff;
    --backdrop: #e7e8ef;
    --ink-light: #eef3fa;
    --divider: rgba(255,255,255,0.55);
  }
  * { box-sizing: border-box; margin: 0; padding: 0; }
  html, body { width: 1200px; height: 900px; overflow: hidden; }
  body {
    background: var(--backdrop);
    font-family: "Arimo", Arial, sans-serif;
    position: relative;
  }
  .card {
    position: absolute;
    top: 294px;
    width: 540px;
    height: 312px;
    border-radius: 22px;
    overflow: hidden;
    box-shadow: 0 6px 18px rgba(20,30,60,0.25);
  }

  /* Back side */
  .card--back { left: 40px; background: var(--brand-blue); }
  .card--back .brand-name {
    position: absolute; left: 0; right: 0; top: 84px;
    text-align: center;
    color: var(--brand-gold);
    font-size: 38px; font-weight: 700; letter-spacing: 1px;
  }
  .card--back .brand-mark {
    position: absolute; left: 96px; top: 90px;
    width: 28px; height: 28px; border-radius: 50%;
    background: var(--brand-gold);
  }
  .card--back .gold-band {
    position: absolute; left: 0; right: 0; top: 196px; height: 22px;
    background: var(--brand-gold);
  }
  .card--back .website {
    position: absolute; left: 0; right: 0; top: 224px;
    text-align: center; color: var(--ink-light); font-size: 17px;
  }

  /* Front side */
  .card--front { left: 620px; background: var(--paper); border: 2px solid #dfe2ea; }
  .card--front .brand-name {
    position: absolute; left: 0; right: 0; top: 48px;
    text-align: center;
    color: var(--brand-blue);
    font-size: 36px; font-weight: 700; letter-spacing: 1px;
  }
  .card--front .brand-mark {
    position: absolute; left: 108px; top: 54px;
    width: 26px; height: 26px; border-radius: 50%;
    background: var(--brand-blue);
  }
  .info-panel {
    position: absolute; left: 0; right: 0; top: 167px; bottom: 0;
    background: var(--brand-blue);
  }
  .name-tab {
    position: absolute; left: 164px; top: 151px; width: 212px; height: 54px;
    background: var(--paper); border-radius: 10px;
    text-align: center; padding-top: 8px;
  }
  .person-name {
    font-family: "Libre Baskerville", Georgia, serif;
    font-variant: small-caps; font-weight: 700;
    color: var(--brand-blue); font-size: 17px;
  }
  .person-role { color: var(--brand-blue); font-size: 13px; margin-top: 4px; }

  .address {
    position: absolute; left: 22px; top: 224px;
    color: var(--ink-light); font-size: 12.5px; line-height: 17px;
  }
  .web-block {
    position: absolute; left: 188px; top: 224px; width: 170px;
    border-left: 1px solid var(--divider); border-right: 1px solid var(--divider);
    padding: 2px 0 2px 16px;
    color: var(--ink-light);
  }
  .web-block .website { font-size: 14px; }
  .web-block .toll-free { font-size: 11.5px; margin-top: 8px; }
  .phones {
    position: absolute; left: 372px; top: 222px;
    color: var(--ink-light); font-size: 14px;
  }
  .phone-line { display: flex; align-items: center; gap: 12px; height: 28px; }
  .phone-line svg { width: 15px; height: 15px; fill: var(--ink-light); }
  .email-tab {
    position: absolute; left: 170px; top: 283px; width: 214px; height: 34px;
    background: var(--paper); border-radius: 10px 10px 0 0;
    text-align: center; padding-top: 7px;
    color: var(--brand-blue); font-size: 13px;
  }
</style>
</head>
<body>

  <section class="card card--back" aria-label="Business card back">
    <span class="brand-mark"></span>
    <div class="brand-name">OL TAVIRAN GROUP</div>
    <div class="gold-band"></div>
    <div class="website">www.oltaviran.com</div>
  </section>

  <section class="card card--front" aria-label="Business card front">
    <span class="brand-mark"></span>
    <div class="brand-name">OL TAVIRAN GROUP</div>
    <div class="info-panel"></div>

    <div class="name-tab">
      <div class="person-name">Selim OR Haddani</div>
      <div class="person-role">Operation Manager</div>
    </div>

    <div class="address">P.O. Box: 12345,<br>Dubai<br>United Arab Emirates</div>

    <div class="web-block">
      <div class="website">www.oltaviran.com</div>
      <div class="toll-free">Toll-Free: (123) 456-7890</div>
    </div>

    <div class="phones">
      <div class="phone-line">
        <svg viewBox="0 0 16 16" aria-hidden="true"><path d="M2 5c0-2 3-3 6-3s6 1 6 3v1h-3V5H5v1H2z M4 7h8l2 6H2z"/></svg>
        <span>(123) 456-7890</span>
      </div>
      <div class="phone-line">
        <svg viewBox="0 0 16 16" aria-hidden="true"><path d="M2 2h12v12H2z M4 4v4h8V4z M4 10v2h2v-2z M7 10v2h2v-2z M10 10v2h2v-2z"/></svg>
        <span>(123) 456-7890</span>
      </div>
    </div>

    <div class="email-tab">selim@oltaviran.com</div>
  </section>

</body>
</html>
```